Independence Day Graphics for Sale

I want to create 10 social media graphics (new Pixtaloo size 4:5 (1080 x 1350 pixels) focusing on our July 4th Sale Graphics, using any of the pics attached. Use the attached pics, NO RANDOM STOCK PHOTOGRAPHY. For the color scheme of the graphics, they should all be complementary to the product colors in the photos.
You can add any of the photos attached but none are required. You can do some of the graphics in all text. I mainly need BOLD text that says one of the headlines (10 total) SEE ATTACHED WORD DOCUMENT for the headlines to use.

Target Market(s)

women looking to lose weight

Requirements
Must have
• pics attached and text attached

```html
<!DOCTYPE html>
<html lang="en">
<head>
<meta charset="utf-8">
<title>July 4th Sale Social Graphics</title>
<link rel="stylesheet" href="https://fonts.googleapis.com/css2?family=Bebas+Neue&display=swap">
<style>
:root{
  --board:#a8a9ad;
  --purple-deep:#7b4f8c;
  --purple-light:#9d63ad;
  --blue-deep:#2f4ea1;
  --blue-light:#5f7fc2;
  --magenta:#b44a8b;
  --pink-light:#e07cae;
  --green-deep:#405f4f;
  --green-light:#94c1b1;
  --headline-blue:#2e4da0;
  --headline-magenta:#b3468a;
  --white:#ffffff;
  --counter:#efeded;
}
*{margin:0;padding:0;box-sizing:border-box}
html,body{width:1200px;height:600px;overflow:hidden;background:var(--board)}
body{font-family:"Bebas Neue",sans-serif}
.board{position:relative;width:1200px;height:600px}
.tile{position:absolute;width:226px;height:282px;overflow:hidden;background:var(--white)}
.tile svg.shape{position:absolute;inset:0;width:100%;height:100%}
.photo{position:absolute}
.photo--model{background:linear-gradient(180deg,#2a2226 0%,#6b4a3d 22%,#f4f2f3 38%,#f0eeef 52%,#9a6a52 62%,#1f1d24 80%,#1f1d24 100%);border-radius:40px 40px 0 0}
.photo--bottles{background:linear-gradient(90deg,#f2f2f4,#ffffff 30%,#e9e6ee 55%,#ffffff 75%,#eef0f6);border-radius:6px}
.counter{position:absolute;left:0;right:0;bottom:0;background:var(--counter)}
.line{position:absolute;line-height:1;white-space:nowrap;text-transform:uppercase;color:var(--white)}
.line.centered{left:0;right:0;text-align:center}
.blue{color:var(--headline-blue)}
.magenta{color:var(--headline-magenta)}
.ord{font-size:.5em;position:relative;top:-.7em}
</style>
</head>
<body>
<main class="board">

  <section class="tile" style="left:10px;top:11px;background:var(--purple-light)">
    <svg class="shape" viewBox="0 0 226 282" preserveAspectRatio="none"><path d="M0 0H120C190 10 226 60 226 110V240H45C18 240 0 222 0 200Z" fill="var(--purple-deep)"/></svg>
    <div class="counter" style="height:46px"></div>
    <div class="photo photo--model" role="img" aria-label="Smiling woman in white cropped sweater holding a supplement bottle" style="left:135px;top:32px;width:91px;height:205px"></div>
    <div class="photo photo--bottles" role="img" aria-label="Two supplement bottles on a counter" style="left:150px;top:214px;width:40px;height:39px"></div>
    <div class="line" style="left:15px;top:25px;font-size:39px">July 4<span class="ord">th</span></div>
    <div class="line" style="left:15px;top:61px;font-size:57px">Mega</div>
    <div class="line" style="left:15px;top:111px;font-size:57px">Sale!</div>
    <div class="line" style="left:15px;top:160px;font-size:36px">25% Off</div>
    <div class="line" style="left:15px;top:192px;font-size:27px">Everything</div>
  </section>

  <section class="tile" style="left:248px;top:11px;background:var(--blue-light)">
    <svg class="shape" viewBox="0 0 226 282" preserveAspectRatio="none"><path d="M0 0H110C180 10 226 60 226 110V255H55C22 255 0 235 0 205Z" fill="var(--blue-deep)"/></svg>
    <div class="counter" style="height:28px"></div>
    <div class="photo photo--model" role="img" aria-label="Smiling woman in white cropped sweater pointing at supplements" style="left:119px;top:29px;width:107px;height:225px"></div>
    <div class="photo photo--bottles" role="img" aria-label="Three supplement bottles on a counter" style="left:137px;top:229px;width:65px;height:40px"></div>
    <div class="line" style="left:19px;top:33px;font-size:36px">Biggest</div>
    <div class="line" style="left:19px;top:64px;font-size:29px">4<span class="ord">th</span> of July</div>
    <div class="line" style="left:19px;top:86px;font-size:54px">Sale</div>
    <div class="line" style="left:19px;top:131px;font-size:50px">Ever!</div>
    <div class="line" style="left:19px;top:175px;font-size:34px">25% Off</div>
    <div class="line" style="left:19px;top:202px;font-size:31px">Sitewide</div>
  </section>

  <section class="tile" style="left:487px;top:11px">
    <div class="line centered magenta" style="top:17px;font-size:55px">Historic</div>
    <div class="line centered magenta" style="top:64px;font-size:46px">4<span class="ord">th</span> of July</div>
    <div class="line centered blue" style="top:103px;font-size:86px">Sale!</div>
    <div class="line centered blue" style="top:179px;font-size:54px">25% Off</div>
    <div class="line centered magenta" style="top:228px;font-size:36px">Of Everything</div>
  </section>

  <section class="tile" style="left:725px;top:11px;background:var(--green-light)">
    <svg class="shape" viewBox="0 0 226 282" preserveAspectRatio="none"><path d="M0 0H140C200 20 226 70 226 110V254H45C18 254 0 235 0 205Z" fill="var(--green-deep)"/></svg>
    <div class="counter" style="height:28px"></div>
    <div class="photo photo--model" role="img" aria-label="Smiling woman in white cropped sweater pointing at supplements" style="left:115px;top:14px;width:111px;height:240px"></div>
    <div class="photo photo--bottles" role="img" aria-label="Three supplement bottles on a counter" style="left:135px;top:228px;width:70px;height:41px"></div>
    <div class="line" style="left:20px;top:28px;font-size:46px">Mega</div>
    <div class="line" style="left:20px;top:70px;font-size:31px">Summer</div>
    <div class="line" style="left:20px;top:102px;font-size:27px">Blowout!</div>
    <div class="line" style="left:20px;top:122px;font-size:57px">25%</div>
    <div class="line" style="left:20px;top:167px;font-size:57px">Off</div>
    <div class="line" style="left:20px;top:216px;font-size:23px">Everything</div>
  </section>

  <section class="tile" style="left:964px;top:11px;background:linear-gradient(180deg,#ffffff 55%,#ecebee 100%)">
    <div class="line centered magenta" style="top:30px;font-size:34px">One-Time Only:</div>
    <div class="line centered blue" style="top:60px;font-size:61px">25% Off</div>
    <div class="line centered blue" style="top:115px;font-size:34px">Of Everything!</div>
    <div class="photo photo--bottles" role="img" aria-label="Row of four supplement bottles" style="left:11px;top:179px;width:205px;height:84px"></div>
  </section>

  <section class="tile" style="left:10px;top:306px;background:linear-gradient(180deg,#ffffff 40%,#e9e8eb 100%)">
    <div class="line centered blue" style="top:24px;font-size:46px">25% Off</div>
    <div class="line centered blue" style="top:71px;font-size:24px">Stock-Up Event:</div>
    <div class="line centered magenta" style="top:94px;font-size:49px">25% Off</div>
    <div class="line centered magenta" style="top:136px;font-size:24px">All Supplements</div>
    <div class="photo photo--bottles" role="img" aria-label="Group of four supplement bottles" style="left:25px;top:174px;width:170px;height:97px"></div>
  </section>

  <section class="tile" style="left:248px;top:306px">
    <div class="line centered magenta" style="top:29px;font-size:39px">The Lowest</div>
    <div class="line centered magenta" style="top:65px;font-size:64px">Prices</div>
    <div class="line centered blue" style="top:120px;font-size:39px">We've Ever</div>
    <div class="line centered blue" style="top:157px;font-size:48px">Offered!</div>
    <div class="line centered magenta" style="top:201px;font-size:55px">25% Off</div>
  </section>

  <section class="tile" style="left:487px;top:306px;background:var(--pink-light)">
    <svg class="shape" viewBox="0 0 226 282" preserveAspectRatio="none"><path d="M0 0H140C200 20 226 70 226 110V249H45C18 249 0 230 0 205Z" fill="var(--magenta)"/></svg>
    <div class="counter" style="height:33px"></div>
    <div class="photo photo--model" role="img" aria-label="Smiling woman in white cropped sweater holding a supplement bottle" style="left:118px;top:26px;width:108px;height:223px"></div>
    <div class="photo photo--bottles" role="img" aria-label="Two supplement bottles on a counter" style="left:138px;top:226px;width:45px;height:38px"></div>
    <div class="line" style="left:9px;top:16px;font-size:25px">Our Biggest</div>
    <div class="line" style="left:9px;top:38px;font-size:32px">Discount</div>
    <div class="line" style="left:9px;top:65px;font-size:47px">Ever!</div>
    <div class="line" style="left:9px;top:105px;font-size:64px">25%</div>
    <div class="line" style="left:9px;top:155px;font-size:64px">Off</div>
    <div class="line" style="left:9px;top:211px;font-size:25px">Everything</div>
  </section>

  <section class="tile" style="left:725px;top:306px;background:var(--purple-light)">
    <svg class="shape" viewBox="0 0 226 282" preserveAspectRatio="none"><path d="M0 0H150C205 20 226 70 226 110V282H0Z" fill="var(--purple-deep)"/></svg>
    <div class="photo photo--model" role="img" aria-label="Smiling woman in white cropped sweater pointing at supplements" style="left:92px;top:14px;width:124px;height:256px"></div>
    <div class="photo photo--bottles" role="img" aria-label="Three supplement bottles" style="left:105px;top:226px;width:73px;height:32px"></div>
    <div class="line" style="left:13px;top:29px;font-size:36px">Don't</div>
    <div class="line" style="left:13px;top:63px;font-size:36px">Wait!</div>
    <div class="line" style="left:13px;top:96px;font-size:43px">25%</div>
    <div class="line" style="left:13px;top:131px;font-size:50px">Off</div>
    <div class="line" style="left:13px;top:174px;font-size:36px">Ends</div>
    <div class="line" style="left:13px;top:201px;font-size:38px">Soon</div>
  </section>

  <section class="tile" style="left:964px;top:306px;background:var(--green-light)">
    <svg class="shape" viewBox="0 0 226 282" preserveAspectRatio="none"><path d="M0 0H120C190 15 226 70 226 110V282H0Z" fill="var(--green-deep)"/></svg>
    <div class="photo photo--model" role="img" aria-label="Smiling woman in white cropped sweater pointing at supplements" style="left:86px;top:34px;width:135px;height:240px"></div>
    <div class="photo photo--bottles" role="img" aria-label="Row of supplement bottles and serum tubes" style="left:53px;top:216px;width:170px;height:58px"></div>
    <div class="line" style="left:19px;top:15px;font-size:36px">Last</div>
    <div class="line" style="left:19px;top:51px;font-size:23px">Chance</div>
    <div class="line" style="left:19px;top:72px;font-size:41px">25%</div>
    <div class="line" style="left:19px;top:109px;font-size:44px">Off</div>
    <div class="line" style="left:19px;top:149px;font-size:25px">Time Is</div>
    <div class="line" style="left:19px;top:173px;font-size:24px">Running</div>
    <div class="line" style="left:19px;top:196px;font-size:23px">Out!</div>
  </section>

</main>
</body>
</html>
```